verdant terraces simple classy business card design

my name is owen harlow and I run a gardening business aimed at high class verdant terraces. the business name is verdant terraces and our logo was designed on pixel forum .My clientel are anything from residential homes to businesses. I take pride in my work and know that I offer a service like no other in my area.
The business card will be used to represent my business and I want it to be not only rememberable, but simplistic and modern. Eye catching too. Of course I would like it relatable to gardening and appealing to the correct clientel - those being garden enthusiasts, prestigious homes and businesses that are after top of the line gardening services like no other on the market.
I am not a typical lawn mowing business so I don't want a typical card design that represents that. The gardens I work with are generally million dollar properties with owners who are very garden proud looking for upkeep and guidance from me along with sometimes whole new garden designs. I want the business cards to show to my clients that I take pride, as they do, in their garden. And I want them to know from my card that I am a professional, qualified horticulturist offering them a top of the line service for life. I want them to refer my business on. I want them to look at my business card and see class and professionalism in a modern unique bold way.
The card should be simple with the possibility of the logo on the front being embossed/debossed and my details on the back the card should have a organic garden feel it's very important to me that it is absolutely perfect
I am also very open to ideas and suggestions so look forward to seeing the designs. the business logo has been supplied with this project and I want the card to be double sided

Contact info is
Owen Harlow - Managing Director / Horticulturist
Phone : 0481 526 704
Email: owenharlow@verdantterraces.com.au

Target Market(s)

high class gardens residential and commercial

Industry/Entity Type

Gardener

Contact Information for Business Card

Contact info is
Phone : 0481 526 704

PLEASE MAKE CARD DOUBLE SIDED

Requirements
Must have
• organic simple classy modern feel
• must flow with the current logo that has been supplied with this project
• Double sided
• Must explain in a simple way that I deal with high end gardens and I'm a qualified horticulturist
Nice to have
• embossed debossed logo
Should not have
• shouldn't be to busy or cheap looking

```html
<!DOCTYPE html>
<html lang="en">
<head>
<meta charset="utf-8">
<title>Verdant Terraces — Business Card</title>
<link href="https://fonts.googleapis.com/css2?family=Quicksand:wght@400;500&display=swap" rel="stylesheet">
<style>
  :root{
    --ink:#3d4a52;
    --mint:#dcf5e3;
    --mint-deep:#cdeed8;
    --gold-a:#d4c195;
    --gold-b:#f0e7c0;
    --gold-c:#d2be90;
    --gold-line:#d8c39c;
    --frame-grey:#5a646a;
    --paper:#ffffff;
    --stage:#eef1f2;
  }
  *{box-sizing:border-box;margin:0;padding:0}
  html,body{width:1200px;height:1200px;overflow:hidden}
  body{
    position:relative;
    font-family:"Quicksand",sans-serif;
    color:var(--ink);
    background:linear-gradient(var(--paper) 0 300px,var(--stage) 300px 100%);
  }
  .card{
    position:absolute;width:494px;height:288px;
    box-shadow:3px 4px 6px rgba(0,0,0,.28);
  }
  .card--front{background:var(--paper)}
  .card--back{background:var(--mint)}
  .row-1{top:62px}
  .row-2{top:520px}
  .col-1{left:72px}
  .col-2{left:636px}

  .motif-band{
    position:absolute;left:72px;top:57px;width:350px;height:175px;
    background:var(--mint);
  }
  .logo-plate{
    position:absolute;left:93px;top:88px;width:307px;height:115px;
    display:flex;flex-direction:column;align-items:center;justify-content:center;gap:10px;
  }
  .logo-plate--gold{background:linear-gradient(90deg,var(--gold-a),var(--gold-b) 50%,var(--gold-c))}
  .logo-plate--white{background:var(--paper)}
  .logo-dot{width:30px;height:30px;border-radius:50%;background:var(--ink)}
  .logo-name{
    font-weight:500;font-size:19px;letter-spacing:3px;text-transform:uppercase;color:var(--ink);
  }

  .details-frame{
    position:absolute;left:60px;top:76px;width:365px;height:130px;
    display:flex;flex-direction:column;align-items:center;justify-content:center;
  }
  .details-frame--gold{border:4px solid var(--gold-line)}
  .details-frame--grey{border:1.5px solid var(--frame-grey)}
  .person-name{font-weight:500;font-size:19px;letter-spacing:3.5px;margin-bottom:10px}
  .person-role{font-size:12.5px;letter-spacing:2px;margin-bottom:6px}
  .contact{display:flex;align-items:center;gap:4px;letter-spacing:1.6px}
  .contact--email{font-size:10.5px;margin-bottom:7px}
  .contact--phone{font-size:12.5px}
  .contact svg{flex:none}

  .caption{
    position:absolute;right:62px;top:1088px;
    font-size:34px;font-weight:400;letter-spacing:1px;color:#111;
  }
</style>
</head>
<body>

  <!-- Gold variation: front -->
  <section class="card card--front row-1 col-1">
    <div class="motif-band" role="img" aria-label="Mint diamond motif behind the logo"></div>
    <div class="logo-plate logo-plate--gold">
      <span class="logo-dot"></span>
      <span class="logo-name">Verdant Terraces</span>
    </div>
  </section>

  <!-- Gold variation: back -->
  <section class="card card--back row-1 col-2">
    <div class="details-frame details-frame--gold">
      <p class="person-name">Owen Harlow</p>
      <p class="person-role">Managing Director / Horticulturist</p>
      <p class="contact contact--email">
        <svg width="15" height="11" viewBox="0 0 15 11" fill="none" stroke="currentColor" stroke-width="1"><rect x=".5" y=".5" width="14" height="10"/><path d="M.5 .5 7.5 6 14.5 .5"/></svg>
        owenharlow@verdantterraces.com.au
      </p>
      <p class="contact contact--phone">
        <svg width="9" height="14" viewBox="0 0 9 14" fill="none" stroke="currentColor" stroke-width="1"><rect x=".5" y=".5" width="8" height="13" rx="1.5"/><path d="M3 11.5h3"/></svg>
        0481 526 704
      </p>
    </div>
  </section>

  <!-- Mint variation: back -->
  <section class="card card--back row-2 col-1">
    <div class="details-frame details-frame--grey">
      <p class="person-name">Owen Harlow</p>
      <p class="person-role">Managing Director / Horticulturist</p>
      <p class="contact contact--email">
        <svg width="15" height="11" viewBox="0 0 15 11" fill="none" stroke="currentColor" stroke-width="1"><rect x=".5" y=".5" width="14" height="10"/><path d="M.5 .5 7.5 6 14.5 .5"/></svg>
        owenharlow@verdantterraces.com.au
      </p>
      <p class="contact contact--phone">
        <svg width="9" height="14" viewBox="0 0 9 14" fill="none" stroke="currentColor" stroke-width="1"><rect x=".5" y=".5" width="8" height="13" rx="1.5"/><path d="M3 11.5h3"/></svg>
        0481 526 704
      </p>
    </div>
  </section>

  <!-- Mint variation: front -->
  <section class="card card--front row-2 col-2">
    <div class="motif-band" role="img" aria-label="Mint diamond motif behind the logo"></div>
    <div class="logo-plate logo-plate--white">
      <span class="logo-dot"></span>
      <span class="logo-name">Verdant Terraces</span>
    </div>
  </section>

  <p class="caption">Two Color Variations</p>

</body>
</html>
```